Hello Creative Minds!
Our business is after a elegant and classy flyer that draws attention!
The business is Velmora Turf - Lawn Rejuvenation Services. We provide services that maintain a healthy and vibrant green lawn through the tough Australian seasons. The products we use limits the water needed to keep grass green to a minimum - practically none at all! This not only helps the home owner or home seller but the environment by limiting the use of water that is needed to create a green lawn. The products we use are made from natural ingredients that are and pet friendly.
This fly will be our introductory offer to the market. Below are the required points that need to be on the flyer. Attached is the business logo, before & after pictures and 1 example of the LAYOUT not DESIGN of what the flyer should be laid out like or similar to. Feel free to use different 'Lawn Mower' pictures.
All the best; if you need any questions answered please feel free to message.
REQUIRED POINTS (Please re-phrase were possible);
*Instantly restores the natural green colour of grass – year round
*Lasts for up to 3 months
*Substantially reduces watering needs
*Pet friendly
*Stays green during droughts and water restrictions
*UV fade resistant
*Won’t bleed, run, or stain once absorbed into the grass
*Safe for the environment, pets and people
*Works in extreme heat, cold and frost
*Organic and natural – no harmful chemicals
*Reduces the amount of fertilizer
and water used on lawns
*Kerb appeal is essential for getting your property sold for the highest price possible
SERVICES & PRICING
Lawn maintenance (cut & trim) starting from $60
Lawn rejuvenation starting from $80 (Only $27 a month for 3 months)*
Package deal starting from $120
Introductory offer: 25% off all services. Refer a friend, when they book you receive another 25% off your next service.
LOCATIONS
Nowra to Sydney
CONTACT NUMBER
Will be posted with the winner - please leave an area for this.
SOCIAL MEDIA
Please add Chatterloop and Snapvista logo's
Updates
Competition has finished, thank you to all that have participated! I will review and comment on the flyers that need assistance. All the best with future designs!
Target Market(s)
home owners, home sellers, property developers, real estates and nursing homes and government housing.
Industry/Entity Type
Lawn Care
Look and feel
Each slider illustrates characteristics of the customer's brand and the style your logo design should communicate.

```html
<!DOCTYPE html>
<html lang="en">
<head>
<meta charset="utf-8">
<title>Velmora Turf - Lawn Rejuvenation Services</title>
<link rel="stylesheet" href="https://fonts.googleapis.com/css2?family=Montserrat:wght@400;500;600;700&family=Oswald:wght@500;600;700&display=swap">
<style>
  :root{
    --navy:#232a36;
    --lime:#86bf24;
    --lime-dark:#6da31a;
    --ink:#2b2b2b;
    --page:#d6d6d6;
    --white:#ffffff;
  }
  *{margin:0;padding:0;box-sizing:border-box}
  html,body{width:703px;height:1200px;overflow:hidden;background:var(--page);font-family:'Montserrat',sans-serif;color:var(--ink)}
  .flyer{position:absolute;left:0;top:103px;width:703px;height:993px;overflow:hidden;box-shadow:0 6px 18px rgba(0,0,0,.25)}
  .flyer-bg{position:absolute;inset:0}
  .brand{position:absolute;left:470px;top:72px;width:240px;text-align:center;color:var(--white)}
  .brand-name{font-family:'Montserrat',sans-serif;font-weight:600;font-size:30px;letter-spacing:.5px;line-height:1}
  .brand-tag{font-size:7px;letter-spacing:2.4px;font-weight:600;margin-top:6px}
  .ba-label{position:absolute;color:var(--white);font-weight:700;font-size:11.5px;letter-spacing:.3px}
  .section-tag{position:absolute;left:31px;top:443px;width:180px;height:38px;background:var(--lime);color:var(--navy);font-weight:700;font-size:19px;display:flex;align-items:center;padding-left:12px;letter-spacing:.3px}
  .features{position:absolute;list-style:none;top:0}
  .features li{position:absolute;left:0;height:0}
  .feature-icon{position:absolute;left:0;top:-15px;width:30px;height:30px;border:1.5px solid var(--lime);border-radius:50%;display:flex;align-items:center;justify-content:center}
  .feature-text{position:absolute;left:47px;top:0;transform:translateY(-50%);font-weight:600;font-size:13.2px;line-height:1.22}
  .features-left{left:32px}
  .features-left .feature-text{width:245px}
  .features-right{left:383px}
  .features-right .feature-text{left:46px;width:230px}
  .price{position:absolute;left:31px;width:244px;height:68px;border-radius:6px;overflow:hidden;display:flex}
  .price-label{flex:1;background:var(--lime);padding:10px 0 0 14px;color:var(--navy)}
  .price-label strong{display:block;font-family:'Oswald',sans-serif;font-weight:600;font-size:17px;line-height:1.05}
  .price-label small{display:block;font-size:6px;margin-top:4px;color:#2e3a1a}
  .price-value{width:98px;background:var(--navy);clip-path:polygon(18% 0,100% 0,100% 100%,0 100%);color:var(--white);font-family:'Oswald',sans-serif;font-weight:700;font-size:36px;display:flex;align-items:center;justify-content:center;padding-left:10px}
  .price-value sup{font-size:18px;margin-right:4px;vertical-align:14px}
  .offer{position:absolute;width:122px;height:122px;border:3px solid var(--lime);border-radius:50%;background:var(--white);text-align:center;display:flex;flex-direction:column;align-items:center;justify-content:center}
  .offer-title{font-family:'Oswald',sans-serif;font-weight:600;font-size:15.5px;line-height:1.1;color:var(--navy)}
  .offer-amount{font-family:'Oswald',sans-serif;font-weight:600;color:var(--lime);font-size:32px;line-height:1.1}
  .offer-amount sup{font-size:18px;vertical-align:10px;margin-right:3px}
  .intro .offer-title{color:var(--lime);font-size:13px}
  .intro-amount{font-family:'Oswald',sans-serif;font-weight:700;font-size:32px;color:var(--navy);display:flex;align-items:flex-end;line-height:1}
  .intro-amount sup{font-size:18px;align-self:flex-start;margin-right:3px}
  .intro-amount span{font-family:'Montserrat',sans-serif;font-size:8px;font-weight:600;text-align:left;line-height:1.05;margin-left:2px;padding-bottom:3px}
  .intro-note{font-size:5px;line-height:1.3;width:88px;margin-top:5px;color:#444}
  .footer{position:absolute;left:0;top:943px;width:703px;height:50px;color:var(--navy)}
  .footer-call{position:absolute;left:29px;top:13px;font-size:18px;color:var(--white);letter-spacing:.3px;white-space:nowrap}
  .footer-call b{font-weight:700;color:var(--navy);font-size:21px}
  .footer-area{position:absolute;left:363px;top:13px;font-size:19px;font-weight:500;white-space:nowrap}
  .divider{position:absolute;top:12px;width:1.5px;height:26px;background:var(--navy)}
  .social{position:absolute;left:556px;top:20px;display:flex;align-items:center;gap:3px;font-size:6px;font-weight:500;white-space:nowrap}
  .social i{display:inline-block;width:7px;height:7px;background:var(--navy);border-radius:1px;margin-left:2px}
</style>
</head>
<body>
<main class="flyer">
  <svg class="flyer-bg" width="703" height="993" viewBox="0 0 703 993" xmlns="http://www.w3.org/2000/svg">
    <defs>
      <linearGradient id="lawnTone" x1="0" y1="0" x2="0" y2="1">
        <stop offset="0" stop-color="#2f5a20"/>
        <stop offset=".25" stop-color="#5aa832"/>
        <stop offset="1" stop-color="#4a9a2c"/>
      </linearGradient>
      <linearGradient id="strawTone" x1="0" y1="0" x2="0" y2="1">
        <stop offset="0" stop-color="#cdb685"/><stop offset="1" stop-color="#a88c58"/>
      </linearGradient>
      <linearGradient id="greenTone" x1="0" y1="0" x2="0" y2="1">
        <stop offset="0" stop-color="#5f8a3a"/><stop offset="1" stop-color="#3f7226"/>
      </linearGradient>
      <linearGradient id="yardTone" x1="0" y1="0" x2="0" y2="1">
        <stop offset="0" stop-color="#555b5f"/><stop offset=".45" stop-color="#6f8a4c"/><stop offset=".7" stop-color="#8e8d86"/><stop offset="1" stop-color="#7b7a76"/>
      </linearGradient>
      <clipPath id="bigLens"><circle cx="404" cy="393" r="110"/></clipPath>
      <clipPath id="smallLens"><circle cx="585" cy="438" r="81"/></clipPath>
    </defs>
    <rect width="703" height="993" fill="var(--navy)"/>
    <rect width="703" height="555" fill="url(#lawnTone)" role="img" aria-label="Photo of a lawn mower on freshly cut green grass"/>
    <rect x="0" y="399" width="310" height="9" fill="var(--navy)"/>
    <path d="M0,408 H310 L640,500 L703,556 V935 H40 Q0,935 0,895 Z" fill="var(--white)"/>
    <circle cx="689" cy="54" r="258" fill="var(--navy)"/>
    <circle cx="404" cy="393" r="116" fill="var(--lime)"/>
    <circle cx="404" cy="393" r="112" fill="var(--white)"/>
    <g clip-path="url(#bigLens)" role="img" aria-label="Before and after photo of dry lawn restored to green">
      <rect x="294" y="283" width="110" height="220" fill="url(#strawTone)"/>
      <rect x="404" y="283" width="110" height="220" fill="url(#greenTone)"/>
      <rect x="294" y="378" width="220" height="26" fill="rgba(60,60,60,.75)"/>
    </g>
    <circle cx="404" cy="391" r="10" fill="none" stroke="#fff" stroke-width="1.5"/>
    <path d="M400,391 l-3,-3 v6 z M408,391 l3,-3 v6 z" fill="#fff"/>
    <circle cx="585" cy="438" r="86" fill="var(--lime)"/>
    <circle cx="585" cy="438" r="83" fill="var(--white)"/>
    <g clip-path="url(#smallLens)" role="img" aria-label="Before and after photo of a front yard lawn beside a driveway">
      <rect x="504" y="357" width="162" height="162" fill="url(#yardTone)"/>
      <rect x="504" y="428" width="162" height="20" fill="rgba(60,60,60,.75)"/>
    </g>
    <circle cx="585" cy="438" r="8.5" fill="none" stroke="#fff" stroke-width="1.3"/>
    <path d="M582,438 l-2.5,-2.5 v5 z M588,438 l2.5,-2.5 v5 z" fill="#fff"/>
    <path d="M0,943 H660 Q703,943 703,985 V993 H0 Z" fill="var(--lime)"/>
  </svg>

  <div class="brand">
    <div class="brand-name">Velmora Turf</div>
    <div class="brand-tag">LAWN REJUVENATION SERVICES</div>
  </div>

  <span class="ba-label" style="left:323px;top:384px">BEFORE</span>
  <span class="ba-label" style="left:431px;top:384px">AFTER</span>
  <span class="ba-label" style="left:518px;top:431px;font-size:10.5px">BEFORE</span>
  <span class="ba-label" style="left:605px;top:431px;font-size:10.5px">AFTER</span>

  <div class="section-tag">OUR SERVICES</div>

  <ul class="features features-left">
    <li style="top:526px"><span class="feature-icon"><svg width="14" height="14" viewBox="0 0 14 14"><path d="M2,7 l3,3 l7,-7" fill="none" stroke="var(--lime-dark)" stroke-width="2"/></svg></span><span class="feature-text">Instantly restores the natural green colour of grass – year round</span></li>
    <li style="top:570px"><span class="feature-icon"><svg width="14" height="14" viewBox="0 0 14 14"><path d="M2,7 l3,3 l7,-7" fill="none" stroke="var(--lime-dark)" stroke-width="2"/></svg></span><span class="feature-text">Lasts for up to 3 months</span></li>
    <li style="top:602px"><span class="feature-icon"><svg width="14" height="14" viewBox="0 0 14 14"><path d="M2,7 l3,3 l7,-7" fill="none" stroke="var(--lime-dark)" stroke-width="2"/></svg></span><span class="feature-text">Pet friendly</span></li>
    <li style="top:642px"><span class="feature-icon"><svg width="14" height="14" viewBox="0 0 14 14"><path d="M2,7 l3,3 l7,-7" fill="none" stroke="var(--lime-dark)" stroke-width="2"/></svg></span><span class="feature-text">Stays green during droughts and water restrictions</span></li>
    <li style="top:684px"><span class="feature-icon"><svg width="14" height="14" viewBox="0 0 14 14"><path d="M2,7 l3,3 l7,-7" fill="none" stroke="var(--lime-dark)" stroke-width="2"/></svg></span><span class="feature-text">UV fade resistant</span></li>
    <li style="top:724px"><span class="feature-icon"><svg width="14" height="14" viewBox="0 0 14 14"><path d="M2,7 l3,3 l7,-7" fill="none" stroke="var(--lime-dark)" stroke-width="2"/></svg></span><span class="feature-text">Won’t bleed, run, or stain once absorbed into the grass</span></li>
  </ul>

  <ul class="features features-right">
    <li style="top:557px"><span class="feature-icon"><svg width="14" height="14" viewBox="0 0 14 14"><path d="M2,7 l3,3 l7,-7" fill="none" stroke="var(--lime-dark)" stroke-width="2"/></svg></span><span class="feature-text">Safe for the environment, pets and people</span></li>
    <li style="top:604px"><span class="feature-icon"><svg width="14" height="14" viewBox="0 0 14 14"><path d="M2,7 l3,3 l7,-7" fill="none" stroke="var(--lime-dark)" stroke-width="2"/></svg></span><span class="feature-text">Works in extreme heat, cold and frost</span></li>
    <li style="top:653px"><span class="feature-icon"><svg width="14" height="14" viewBox="0 0 14 14"><path d="M2,7 l3,3 l7,-7" fill="none" stroke="var(--lime-dark)" stroke-width="2"/></svg></span><span class="feature-text">Organic and natural – no harm-ful chemicals</span></li>
    <li style="top:702px"><span class="feature-icon"><svg width="14" height="14" viewBox="0 0 14 14"><path d="M2,7 l3,3 l7,-7" fill="none" stroke="var(--lime-dark)" stroke-width="2"/></svg></span><span class="feature-text">Reduces the amount of fertilizer and water used on lawns</span></li>
    <li style="top:751px"><span class="feature-icon"><svg width="14" height="14" viewBox="0 0 14 14"><path d="M2,7 l3,3 l7,-7" fill="none" stroke="var(--lime-dark)" stroke-width="2"/></svg></span><span class="feature-text">Kerb appeal is essential for getting your property sold for the highest price possible</span></li>
  </ul>

  <div class="price" style="top:766px">
    <div class="price-label"><strong>Lawn rejuvenation<br>starting from</strong><small>Only $27 a month for 3 month</small></div>
    <div class="price-value"><sup>$</sup>80</div>
  </div>
  <div class="price" style="top:844px">
    <div class="price-label"><strong>Lawn maintenance<br>starting from</strong><small>cut &amp; trim</small></div>
    <div class="price-value"><sup>$</sup>60</div>
  </div>

  <div class="offer package" style="left:390px;top:805px">
    <div class="offer-title">Package deal<br>starting from</div>
    <div class="offer-amount"><sup>$</sup>120</div>
  </div>
  <div class="offer intro" style="left:535px;top:805px">
    <div class="offer-title">Introductory offer</div>
    <div class="intro-amount"><sup>$</sup>25<span>off<br>all services</span></div>
    <div class="intro-note">Refer a friend, when they book you receive another 25% off your next service</div>
  </div>

  <footer class="footer">
    <div class="footer-call">CALL US NOW: <b>0491 570 156</b></div>
    <span class="divider" style="left:333px"></span>
    <div class="footer-area">Nowra to Sydney</div>
    <span class="divider" style="left:546px"></span>
    <div class="social"><span>Follow us</span><i></i><span>Chatterloop</span><i></i><span>Snapvista</span></div>
  </footer>
</main>
</body>
</html>
```